Legal Information Website

We need a website that will serve as a source of information for people visiting, living, and working in the United Arab Emirates, where they can go and read about legal issues, laws, crimes, and most important find legal advice and find lawyers. The following are the pages of the website:

Find a Lawyer (Home Page)
This main feature of this page should be "Find a Lawyer"
Find a Lawyer should include the searching option by practice, by lawyer’s name, by law firm name or by location.

Ask a lawyer
This function allows the user to ask a lawyer a legal question and get an answer directly from a lawyer.

Research a legal matter
This function allows the user to do research on a certain legal topic. He/she can select from different legal topics.

Contact Us:
This page should include our contact details for the visitors in case they need any assistance. Contact us by Phone, Email, or Chat.

Once the design is approved, we will provide the rest of the website text.

Target Market(s)

General Public who seek legal advice

Industry/Entity Type

Law Firm

Font styles to use
Serif
Sans Serif

Requirements
Must have
• A tool to search for lawyer's, and then display the lawyer's picture and profile and credentials.

```html
<!DOCTYPE html>
<html lang="en">
<head>
<meta charset="utf-8">
<title>Lexhaven – Find a Lawyer</title>
<link rel="stylesheet" href="https://fonts.googleapis.com/css2?family=Open+Sans:wght@400;600&family=Merriweather:wght@400;700&family=Roboto+Condensed:wght@400;700&display=swap">
<style>
:root{
  --red:#c8161d;
  --red-dark:#8e0007;
  --ink:#333;
  --muted:#7a7a7a;
  --nav:#1e1e1e;
  --panel:#777;
  --date:#8c8c8c;
  --light:#ececec;
  --white:#fff;
}
*{box-sizing:border-box;margin:0;padding:0}
html,body{width:1056px;height:1200px;overflow:hidden}
body{position:relative;background:#fafafa;font-family:"Open Sans",sans-serif;color:var(--ink)}
.abs{position:absolute}

/* header */
.site-header{left:0;top:0;width:1056px;height:123px;background:#f8f8f8}
.brand{left:100px;top:70px;display:flex;align-items:center;gap:10px}
.brand-mark{width:22px;height:22px;background:var(--red)}
.brand-name{font-family:"Merriweather",serif;font-size:26px;font-weight:400;color:#666;letter-spacing:1px}
.contact{left:803px;top:26px;font-size:11.5px;color:#666;line-height:17px}
.contact strong{font-size:13.5px;color:#111;font-weight:600}
.social{left:803px;top:81px;display:flex;gap:5px}
.social span{width:19px;height:19px;border-radius:3px}

/* nav */
.main-nav{left:0;top:123px;width:1056px;height:40px;background:var(--nav)}
.main-nav ul{list-style:none;display:flex;position:absolute;left:108px;top:12px;font-size:12.5px;color:#fff}
.main-nav li+li::before{content:"|";margin:0 19px}
.search{left:764px;top:130px;width:193px;height:24px;background:#fff;border-radius:2px;font-size:11px;color:#888;padding:4px 8px}
.search svg{position:absolute;right:6px;top:4px}

/* hero */
.hero{left:0;top:163px;width:1056px;height:428px;background:linear-gradient(180deg,#e4e4e4 0%,#d6d8da 55%,#c9cacb 100%)}
.hero-band{left:0;top:588px;width:1056px;height:3px;background:#3a3a3a}
.finder{left:129px;top:210px;width:212px;height:273px;background:var(--panel);border-radius:3px;padding:0 8px}
.finder h2{font-weight:400;font-size:17px;color:#fff;padding:5px 3px 6px;border-bottom:1px solid #8c8c8c;margin-bottom:11px}
.finder .field{height:27px;background:#fff;border:1px solid #ccc;margin-bottom:9px;font-size:11px;color:#888;padding:6px 7px}
.finder .btn{display:inline-block;margin-top:6px;background:#eee;padding:6px 9px;font-size:12px;font-weight:600;color:#222}
.hero-photo{left:669px;top:163px;width:290px;height:365px;background:linear-gradient(180deg,#e9d9c6 0%,#2b2b2b 45%,#1c1c1c 100%);border-radius:120px 120px 0 0}
.lower-bg{left:0;top:591px;width:1056px;height:564px;background:linear-gradient(180deg,#d9d9d9 0%,#f6f6f6 60%,#fff 100%)}

/* content panel */
.panel{left:99px;top:530px;width:863px;height:625px;background:#fff}
.section-title{font-size:17px;font-weight:400;color:#333}
.lawyer{left:116px;display:flex;gap:14px}
.lawyer .thumb{width:54px;height:52px;background:linear-gradient(180deg,#d8c2ab,#5a4c44);border:2px solid #fff;box-shadow:0 1px 3px #999}
.lawyer h3{font-size:11.5px;font-weight:400;color:var(--red)}
.lawyer p{font-size:10px;line-height:13px;margin-top:5px;color:#333}
.article{left:412px;display:flex;gap:10px}
.date{width:54px;height:61px;background:var(--date);color:#fff;font-size:19px;line-height:24px;text-align:center;padding-top:6px}
.article p{font-size:11px;line-height:14px;color:var(--muted);width:175px}
.divider{left:412px;top:682px;width:260px;height:1px;background:#ddd}
.more{left:412px;top:788px;font-size:11px;color:#222}
.more b{color:var(--red)}

.topics{left:705px;top:562px;width:236px;height:229px;background:var(--red);border-radius:3px}
.topic{height:57px;display:flex;align-items:center;padding-left:18px;border-bottom:1px solid #a90f15;position:relative}
.topic:last-child{border:0}
.topic .ico{width:40px;height:40px;border-radius:50%;background:#fff;display:flex;align-items:center;justify-content:center;margin-right:12px}
.topic span{font-family:"Roboto Condensed",sans-serif;font-weight:700;font-size:16px;color:#fff}
.topic .go{position:absolute;right:9px;top:23px;width:12px;height:12px;border-radius:50%;background:#7a0005}

.soft-line{left:160px;top:837px;width:740px;height:2px;background:linear-gradient(90deg,transparent,#ccc,transparent)}

/* bottom */
.tab{left:119px;width:237px;height:44px;font-size:21px;font-weight:400;padding:8px 13px}
.tab.active{background:var(--red-dark);color:#fff}
.tab.idle{background:var(--light);color:#555}
.photo2{left:387px;top:876px;width:211px;height:279px;background:linear-gradient(180deg,#d9b9a0 0%,#222 40%,#151515 100%);border-radius:90px 90px 0 0}
.feature{left:608px;top:890px;width:330px}
.feature h2{font-family:"Merriweather",serif;font-weight:400;font-size:21px;color:#444;margin-bottom:13px}
.feature p{font-size:11px;line-height:15px;color:var(--muted);margin-bottom:15px}
.feature p.dark{color:#333}
.dots{display:flex;gap:3px}
.dots i{width:6px;height:6px;border-radius:50%;background:var(--red-dark)}

/* footer */
.site-footer{left:0;top:1155px;width:1056px;height:45px;background:#2e2e2e;color:#fff;font-size:10px}
.site-footer .links{position:absolute;left:106px;top:16px}
.site-footer .copy{position:absolute;right:105px;top:16px}
</style>
</head>
<body>
<header class="site-header abs"></header>
<div class="brand abs"><span class="brand-mark"></span><span class="brand-name">LEXHAVEN</span></div>
<div class="contact abs">Call us today! <strong>971-400-1187</strong><br>Level 4, 18 Cedar Avenue<br>United Arab Emirates</div>
<div class="social abs"><span style="background:#3b5b9a"></span><span style="background:#1b77b5"></span><span style="background:#2bb7ea"></span></div>

<nav class="main-nav abs"><ul><li>Home</li><li>know your rights</li><li>Find a Lawyer</li><li>News</li><li>Articles</li><li>Contact Us</li></ul></nav>
<div class="search abs">Search
  <svg width="17" height="17" viewBox="0 0 17 17"><circle cx="7" cy="7" r="5.5" fill="none" stroke="#666" stroke-width="2"/><line x1="11" y1="11" x2="16" y2="16" stroke="#666" stroke-width="2.4"/></svg>
</div>

<section class="hero abs" role="img" aria-label="Blurred city skyline background"></section>
<div class="lower-bg abs"></div>
<div class="hero-band abs"></div>
<form class="finder abs">
  <h2>Find a Lawyers</h2>
  <div class="field">Lawyer's Name :</div>
  <div class="field">Lawyer Practice :</div>
  <div class="field">Law Firm Name :</div>
  <div class="field">Location :</div>
  <div class="field">About Case</div>
  <span class="btn">FIND A LAWYER</span>
</form>
<div class="hero-photo abs" role="img" aria-label="Photo of a lawyer in a black robe holding an open red law book"></div>

<main class="panel abs"></main>
<h2 class="section-title abs" style="left:116px;top:549px">OUR LAWYERS</h2>
<div class="lawyer abs" style="top:587px"><div class="thumb" role="img" aria-label="Lawyer portrait"></div><div><h3>Mira Haddon</h3><p>On sait depuis longtemps que<br>travailler avec du texte lisible etcon</p></div></div>
<div class="lawyer abs" style="top:658px"><div class="thumb" role="img" aria-label="Lawyer portrait"></div><div><h3>Owen Talbert</h3><p>On sait depuis longtemps que<br>travailler avec du texte lisible etcon</p></div></div>
<div class="lawyer abs" style="top:727px"><div class="thumb" role="img" aria-label="Lawyer portrait"></div><div><h3>Mira Haddon</h3><p>On sait depuis longtemps que<br>travailler avec du texte lisible etcon</p></div></div>

<h2 class="section-title abs" style="left:415px;top:549px">ARTICLES</h2>
<div class="article abs" style="top:597px"><div class="date">Feb<br>19</div><p>It is a long established fact that a reader will be distracted by the readable content of a page when looking at its layout.</p></div>
<div class="divider abs"></div>
<div class="article abs" style="top:711px"><div class="date">Feb<br>12</div><p>It is a long established fact that a reader will be distracted by the readable content of a page when looking at its layout.</p></div>
<div class="more abs">VIEW MORE OUR ARTICLES <b>➔</b></div>

<div class="topics abs">
  <div class="topic"><div class="ico"><svg width="22" height="20" viewBox="0 0 22 20"><path d="M1 6 L11 1 L21 6 Z" fill="#666"/><rect x="3" y="7" width="3" height="9" fill="#666"/><rect x="9.5" y="7" width="3" height="9" fill="#666"/><rect x="16" y="7" width="3" height="9" fill="#666"/><rect x="1" y="17" width="20" height="2" fill="#666"/></svg></div><span>LAWS</span><i class="go"></i></div>
  <div class="topic"><div class="ico"><svg width="22" height="20" viewBox="0 0 22 20"><circle cx="6" cy="5" r="3" fill="#666"/><circle cx="16" cy="5" r="3" fill="#666"/><circle cx="11" cy="8" r="3" fill="#666"/><rect x="3" y="9" width="6" height="9" fill="#666"/><rect x="13" y="9" width="6" height="9" fill="#666"/><rect x="8" y="12" width="6" height="8" fill="#666"/></svg></div><span>LEGAL ISSUES</span><i class="go"></i></div>
  <div class="topic"><div class="ico"><svg width="26" height="26" viewBox="0 0 26 26"><circle cx="13" cy="13" r="11" fill="none" stroke="#666" stroke-width="2"/><circle cx="13" cy="7.5" r="1.6" fill="#666"/><rect x="11.6" y="11" width="2.8" height="9" fill="#666"/></svg></div><span>FIND LEGAL ADVICE</span><i class="go"></i></div>
  <div class="topic"><div class="ico"><svg width="20" height="22" viewBox="0 0 20 22"><rect x="2" y="2" width="16" height="19" fill="none" stroke="#666" stroke-width="2"/><rect x="5" y="5" width="3" height="3" fill="#666"/><rect x="12" y="5" width="3" height="3" fill="#666"/><rect x="5" y="11" width="3" height="3" fill="#666"/><rect x="12" y="11" width="3" height="3" fill="#666"/><rect x="8" y="16" width="4" height="5" fill="#666"/></svg></div><span>FIND LAWYERS</span><i class="go"></i></div>
</div>

<div class="soft-line abs"></div>

<div class="tab active abs" style="top:876px">Law practice</div>
<div class="tab idle abs" style="top:931px">Lawyers profile</div>
<div class="tab idle abs" style="top:986px">View all lawyers</div>
<div class="photo2 abs" role="img" aria-label="Photo of a young lawyer in a black robe holding a red book"></div>
<article class="feature abs">
  <h2>Donec auctor tempor ultrices.</h2>
  <p>It is a long established fact that a reader will be distracted by the readable content of a page when looking at its layout. The point of using Lorem Ipsum is that it has a more-or-less normal distribution of letters, as opposed to using 'Content here, content here', making it look like readable English.</p>
  <p class="dark">Many desktop publishing packages and web page editors now use Lorem Ipsum as their default model text, and a search for 'lorem ipsum' will uncover many web sites still in their infancy. Various versions have evolved over the years, sometimes by accident, sometimes on purpose (injected humour and the like).</p>
  <div class="dots"><i></i><i></i><i></i></div>
</article>

<footer class="site-footer abs">
  <div class="links">site information &nbsp;|&nbsp; disclaimer &nbsp;|&nbsp; internal</div>
  <div class="copy">© 2003-2014 lexhaven, Inc. All rights reserved.</div>
</footer>
</body>
</html>
```